Retirement Plan Advisor Bio

See the attached document and photo for content. I would like someone to design this one page flyer using my logo. This logo was designed by a designer with sketch hive. I am looking for a professional looking document. I want to he color scheme to be primarily white and gold.

Target Market(s)

Employers who offer a retirement plan

Requirements
Should not have
• The designs that I have received look more like resumes. I am interested in advertising my Retirement plan services. If anyone can change their submissions and change it to an ad for retirement plan services instead of a Bio or resume, I would prefer that.

```html
<!DOCTYPE html>
<html lang="en">
<head>
<meta charset="utf-8">
<title>Retirement Plan Services Flyer</title>
<link rel="stylesheet" href="https://fonts.googleapis.com/css2?family=Jost:wght@400;500&family=Montserrat:wght@700;800&display=swap">
<style>
:root{
  --gold:#9a7b3c;
  --gray:#d1d2d4;
  --ink:#231f20;
  --cta-bar:#5c4f3a;
  --white:#ffffff;
}
*{margin:0;padding:0;box-sizing:border-box}
html,body{width:848px;height:1200px;overflow:hidden;background:var(--white)}
body{position:relative;font-family:'Jost',sans-serif;color:var(--ink)}
.hero-photo{position:absolute;left:0;top:0;width:848px;height:281px;
  background:radial-gradient(circle at 300px 110px,#ffd27a 0,#e9913a 60px,rgba(120,110,60,0) 200px),
  linear-gradient(180deg,#6f7b44 0%,#4f6131 55%,#7a8a4a 100%)}
.hero-cut{position:absolute;left:0;top:0}
.brand{position:absolute;left:500px;top:58px;display:flex;align-items:center;gap:8px;white-space:nowrap;
  font-family:'Jost',sans-serif;font-weight:500;color:var(--gold);font-size:23px;letter-spacing:.3px}
.brand-mark{width:20px;height:20px;background:var(--gold)}
.headline-band{position:absolute;left:0;top:281px;width:848px;height:185px;
  background:linear-gradient(100deg,#c9ad74 0%,#b1934f 35%,#8e6f32 100%)}
.headline{position:absolute;left:0;right:0;top:310px;text-align:center;
  font-family:'Montserrat',sans-serif;font-weight:800;color:var(--white);
  font-size:43px;line-height:42px;letter-spacing:-.3px}
.sidebar{position:absolute;left:38px;top:466px;width:291px;height:674px;background:var(--gray)}
.portrait{position:absolute;left:0;top:403px;width:178px;height:230px;border-top-right-radius:70px;
  background:linear-gradient(160deg,#7d95c4 0%,#4f6aa0 60%,#2c2f3a 100%)}
.advisor{position:absolute;left:190px;top:524px;width:136px}
.advisor-name{font-family:'Montserrat',sans-serif;font-weight:800;color:var(--gold);font-size:15.5px;line-height:21px;white-space:nowrap}
.advisor-rule{height:2px;background:var(--gold);margin:5px 0 4px}
.advisor-role{font-size:12px;line-height:19px;white-space:nowrap}
.advisor-email{font-size:10px;display:flex;align-items:center;gap:3px;white-space:nowrap}
.side-block{position:absolute;left:53px;width:260px}
.side-title{font-family:'Montserrat',sans-serif;font-weight:800;color:var(--gold);font-size:16px;line-height:20px}
.ticks{list-style:none}
.ticks li{position:relative;padding-left:27px;font-size:17px;line-height:20.6px}
.ticks li svg{position:absolute;left:7px;top:4px}
.specialties{top:668px}
.qualifications{top:934px}
.main{position:absolute;left:354px;top:484px;width:470px}
.section{margin-bottom:22px}
.section-title{font-family:'Montserrat',sans-serif;font-weight:800;color:var(--gold);font-size:16.5px;line-height:19px}
.section p{font-size:17px;line-height:20.5px}
.cta{position:absolute;left:354px;top:1045px;display:flex;gap:10px}
.cta-bar{width:18px;height:68px;background:var(--cta-bar)}
.cta-text{font-family:'Montserrat',sans-serif;font-weight:800;color:var(--gold);font-size:24px;line-height:31px;padding-top:3px;white-space:nowrap}
.footer{position:absolute;left:0;top:1140px;width:848px;height:60px;background:var(--ink);
  display:flex;align-items:center;justify-content:center;gap:8px;color:var(--white);font-size:19px}
.footer span{display:flex;align-items:center;gap:4px}
.footer .web{font-family:'Montserrat',sans-serif;font-weight:800;color:var(--gold);margin-left:8px}
</style>
</head>
<body>
<div class="hero-photo" role="img" aria-label="Photograph of a multigenerational family outdoors at sunset holding small flags"></div>
<svg class="hero-cut" width="848" height="281" viewBox="0 0 848 281"><polygon points="226,0 848,0 848,174" fill="#ffffff"/></svg>
<div class="brand"><span class="brand-mark"></span>Keystone FINANCIAL, LLC</div>

<div class="headline-band"></div>
<h1 class="headline">COMMITTED TO HELP YOU<br>PURSUE YOUR RETIREMENT<br>FINANCIAL GOALS</h1>

<div class="sidebar"></div>
<div class="portrait" role="img" aria-label="Portrait photograph of the financial advisor"></div>
<div class="advisor">
  <div class="advisor-name">Dana L Whitford<br>CFP®AIF®</div>
  <div class="advisor-rule"></div>
  <div class="advisor-role">Harbor Point Advisor</div>
  <div class="advisor-email"><svg width="11" height="8" viewBox="0 0 11 8"><rect x=".5" y=".5" width="10" height="7" fill="none" stroke="#9a7b3c"/><path d="M.5 .5l5 4 5-4" fill="none" stroke="#9a7b3c"/></svg>dwhitford@harborpt.com</div>
</div>

<div class="side-block specialties">
  <h2 class="side-title">PROFESSIONAL SPECIALTIES</h2>
  <ul class="ticks">
    <li><svg width="13" height="13" viewBox="0 0 13 13"><circle cx="6.5" cy="6.5" r="6.5" fill="#9a7b3c"/><path d="M3.5 6.7l2 2 4-4" stroke="#fff" stroke-width="1.6" fill="none"/></svg>Over 18 years of experience in the retirement plan industry.</li>
    <li><svg width="13" height="13" viewBox="0 0 13 13"><circle cx="6.5" cy="6.5" r="6.5" fill="#9a7b3c"/><path d="M3.5 6.7l2 2 4-4" stroke="#fff" stroke-width="1.6" fill="none"/></svg>Focused on helping plan sponsors reduce administrative burdens and fiduciary risk.</li>
    <li><svg width="13" height="13" viewBox="0 0 13 13"><circle cx="6.5" cy="6.5" r="6.5" fill="#9a7b3c"/><path d="M3.5 6.7l2 2 4-4" stroke="#fff" stroke-width="1.6" fill="none"/></svg>Dedicated to helping employees work toward a positive retirement outcome through careful analysis of their savings rate , investment strategy and overall financial&nbsp; wellness.</li>
  </ul>
</div>

<div class="side-block qualifications">
  <h2 class="side-title">QUALIFICATIONS</h2>
  <ul class="ticks">
    <li><svg width="13" height="13" viewBox="0 0 13 13"><circle cx="6.5" cy="6.5" r="6.5" fill="#9a7b3c"/><path d="M3.5 6.7l2 2 4-4" stroke="#fff" stroke-width="1.6" fill="none"/></svg>Certified Financial Planner®.</li>
    <li><svg width="13" height="13" viewBox="0 0 13 13"><circle cx="6.5" cy="6.5" r="6.5" fill="#9a7b3c"/><path d="M3.5 6.7l2 2 4-4" stroke="#fff" stroke-width="1.6" fill="none"/></svg>Accredited Investment Fiduciary®.</li>
    <li><svg width="13" height="13" viewBox="0 0 13 13"><circle cx="6.5" cy="6.5" r="6.5" fill="#9a7b3c"/><path d="M3.5 6.7l2 2 4-4" stroke="#fff" stroke-width="1.6" fill="none"/></svg>Investment Advisor Representative.</li>
    <li><svg width="13" height="13" viewBox="0 0 13 13"><circle cx="6.5" cy="6.5" r="6.5" fill="#9a7b3c"/><path d="M3.5 6.7l2 2 4-4" stroke="#fff" stroke-width="1.6" fill="none"/></svg>Series 7, 63, and 65 Securities licenses with Harbor Point.</li>
    <li><svg width="13" height="13" viewBox="0 0 13 13"><circle cx="6.5" cy="6.5" r="6.5" fill="#9a7b3c"/><path d="M3.5 6.7l2 2 4-4" stroke="#fff" stroke-width="1.6" fill="none"/></svg>Holds Life and Health Insurance licenses from Illinois.</li>
  </ul>
</div>

<main class="main">
  <section class="section">
    <h2 class="section-title">RETIREMENT PLANNING</h2>
    <p>Many can visualize the retirement of their dreams; traveling, enjoying time with family, volunteering or even pursuing a second career. The hard part is building a financial plan that will afford you this dream. My strategies help you assemble the pieces of this puzzle into an plan. Your vision can be pursued.</p>
  </section>
  <section class="section">
    <h2 class="section-title">INVESTMENT MANAGEMENT</h2>
    <p>Choosing a portfolio of investments is an intimidating process for most. Maintaining a strategy through all phases of the accumulation years and modifying that strategy for the years of spending in retirement is a dynamic process. This is something that I do well. Assessing your risk level and matching it up with a portfolio of investments is key to building your nest egg as well as making it last. My job is to help you live out your retirement years with a sense of financial independence.</p>
  </section>
  <section class="section">
    <h2 class="section-title">RETIREMENT PLAN DEVELOPMENT</h2>
    <p>For the duration of my career I have worked in the 403(b) retirement plan market. The changes in the industry over recent years require employers to be more diligent in their plan offering.&nbsp; Designing a plan that will benefit, both, the employees as well as the employer, choosing a lineup of world class investments, keeping cost down and keeping up with industry regulation all play a part in improving participant outcome. My experience brings experience in all these areas.</p>
  </section>
</main>

<div class="cta"><div class="cta-bar"></div><div class="cta-text">SCHEDULE A COMPLIMENTARY<br>CONSULTATION</div></div>

<footer class="footer">
  <span><svg width="12" height="17" viewBox="0 0 12 17"><path d="M6 0a6 6 0 0 0-6 6c0 4.5 6 11 6 11s6-6.5 6-11a6 6 0 0 0-6-6z" fill="#9a7b3c"/><circle cx="6" cy="6" r="2.2" fill="#231f20"/></svg>240 Maple Ridge Ave. Springfield, IL 62704</span>
  <span><svg width="18" height="18" viewBox="0 0 18 18"><path d="M4 2l3 3-2 2c1 2 3 4 5 5l2-2 3 3-2 3C7 15 2 9 2 4z" fill="none" stroke="#9a7b3c" stroke-width="1.4"/></svg>(555)014.2298</span>
  <span class="web">www.danawhitford.com</span>
</footer>
</body>
</html>
```